Harbor Ridge Labs and VELARA

I'd like to create an announcement which will be posted on our website (www.harborridgelabs.example) that announces our partnership with VELARA, a large Dominican community healthcare service in the greater NYC area. Harbor Ridge Labs (my company) is one of two medical laboratories that are considered "preferred laboratories" for VELARA. I will include an example of what the other preferred laboratory (Trulane laboratory) has on their website.
My website - www.harborridgelabs.example
Velara preferred listings - https://velaracarenet.example/wp-content/uploads/2020/09/5-VELARA-Tier-2-Network-2020-09.pdf
Example of how we helped VELARA clients and the Dominican consulate - https://playamarinoticias.example/consulado-rd-ny-concluye-vuelos-ferry-para-dominicanos-varados-en-ee-uu-por-covid-19/
Trulane announcement on their website - https://www.trulane.example/trulane-laboratories-forms-a-strategic-collaboration-with-velara-to-improve-health-outcomes-of-underserved-new-yorkers/

```html
<!DOCTYPE html>
<html lang="en">
<head>
<meta charset="utf-8">
<title>Harbor Ridge Laboratories</title>
<link href="https://fonts.googleapis.com/css2?family=Montserrat:wght@300;400;700&family=Roboto:wght@400;500;700&display=swap" rel="stylesheet">
<style>
:root{
  --red:#b3121a;
  --navy:#1b2a6b;
  --teal:#3f8f7f;
  --green:#1d7a3a;
  --ink:#222;
  --muted:#666;
  --white:#fff;
  --shade:rgba(0,0,0,.8);
}
*{box-sizing:border-box;margin:0;padding:0}
html,body{width:807px;height:1200px;overflow:hidden}
body{position:relative;background:var(--white);font-family:Roboto,sans-serif;color:var(--ink)}
.alert-bar{position:absolute;top:0;left:0;width:807px;height:32px;background:var(--red);display:flex;align-items:center;justify-content:center;gap:22px;color:#f3d0d0;font:700 10px Roboto,sans-serif}
.alert-bar .read{border:1px solid #e6a5a5;border-radius:3px;padding:4px 9px;font-weight:400;font-size:8px}
.alert-close{position:absolute;right:30px;top:1px;font:700 16px Roboto,sans-serif;color:#fff}
.site-header{position:absolute;top:32px;left:0;width:807px;height:61px;background:var(--white)}
.brand{position:absolute;left:9px;top:34px;font:500 11px Roboto,sans-serif;color:var(--navy);display:flex;align-items:center;gap:5px;white-space:nowrap}
.brand .dot{width:8px;height:8px;border-radius:50%;background:var(--teal)}
.contact{position:absolute;top:18px;display:flex;gap:7px;align-items:flex-start}
.contact svg{width:18px;height:18px;margin-top:2px}
.contact b{display:block;font:700 10px Roboto,sans-serif;color:var(--navy)}
.contact span{font-size:7px;color:var(--muted)}
.main-nav{position:absolute;top:93px;left:0;width:807px;height:73px;background:var(--navy);color:#fff;font:500 8.5px Roboto,sans-serif}
.main-nav .item{position:absolute}
.book{position:absolute;right:18px;top:22px;width:124px;height:31px;background:var(--green);color:#fff;font:700 8px Roboto,sans-serif;text-align:center;padding-top:6px;line-height:1.1}
.hero{position:absolute;top:166px;left:0;width:807px;height:231px;background:linear-gradient(110deg,#5d6f78,#9aa7ae 55%,#c2cacf)}
.hero h1{position:absolute;left:16px;top:30px;font:700 33px/1.05 Montserrat,sans-serif;color:#fff}
.hero p{position:absolute;left:16px;top:118px;font:400 11.5px Montserrat,sans-serif;color:#fff}
.hero .cta{position:absolute;top:137px;height:30px;background:var(--green);color:#cfe;font:500 8.5px Montserrat,sans-serif;text-align:center;padding-top:5px;line-height:1.1}
.intro{position:absolute;top:397px;left:0;width:807px;text-align:center}
.intro h2{margin-top:56px;font:700 28px Montserrat,sans-serif;color:var(--ink)}
.intro h2 em{font-style:normal;color:var(--green)}
.intro hr{width:62px;margin:12px auto 0;border:0;border-top:1px solid #333}
.intro p{margin:14px auto 0;width:700px;font:300 11.5px/1.5 Montserrat,sans-serif;color:var(--muted)}
.card{position:absolute;top:627px;width:316px;height:290px;background:var(--white);box-shadow:0 2px 8px rgba(0,0,0,.12);text-align:center}
.card .photo{height:167px}
.card h3{margin-top:4px;font:300 20px Montserrat,sans-serif;color:var(--ink);line-height:1}
.card h3 strong{display:block;font:700 32px Montserrat,sans-serif;color:var(--green)}
.card p{margin:12px auto 0;width:290px;font:300 9.5px/1.45 Montserrat,sans-serif;color:var(--muted)}
.site-footer{position:absolute;top:1003px;left:0;width:807px;height:157px;background:#f6f6f6;border-top:2px solid var(--green)}
.site-footer .brand{top:72px;left:18px;font-size:12px}
.site-footer .about{position:absolute;left:16px;top:97px;width:210px;font:400 8px/1.9 Roboto,sans-serif;color:var(--muted)}
.newsletter h4{position:absolute;left:420px;top:56px;font:500 11px Roboto,sans-serif;color:var(--navy)}
.newsletter .field{position:absolute;top:75px;width:120px;height:25px;border:1px solid #ccc;background:#fff;font-size:6.5px;color:#999;padding:9px 10px}
.newsletter .sub{position:absolute;left:671px;top:75px;width:120px;height:25px;background:var(--green);color:#fff;font:500 6.5px Roboto,sans-serif;letter-spacing:3px;text-align:center;padding-top:9px}
.legal{position:absolute;top:1160px;left:0;width:807px;height:40px;background:#f6f6f6;border-top:1px solid #ddd;text-align:center;font:400 6.5px Roboto,sans-serif;color:#888;padding-top:15px}
.shade{position:absolute;inset:0;background:var(--shade)}
.modal{position:absolute;left:145px;top:97px;width:517px;height:230px;background:var(--white);display:flex}
.modal .photo{width:214px;height:230px;background:linear-gradient(135deg,#e8eef2,#b9cbd6 50%,#6fb4d6)}
.modal .body{position:relative;flex:1}
.modal .brand{left:33px;top:60px;font-size:11px}
.modal p{position:absolute;left:33px;top:87px;width:250px;font:400 10.5px/1.65 Roboto,sans-serif;color:#111}
.signup{position:absolute;left:33px;top:147px;width:217px;height:32px;border:1px solid #ccc;display:flex;align-items:center}
.signup span{flex:1;padding-left:8px;font-size:8.5px;color:#333}
.signup .send{width:29px;height:28px;margin-right:2px;background:var(--teal);display:flex;align-items:center;justify-content:center}
.links{position:absolute;left:33px;top:186px;display:flex;gap:17px;font:500 9.5px Roboto,sans-serif;letter-spacing:.4px}
.links a{text-decoration:none;border-bottom:1px solid;padding-bottom:1px}
.links .learn{color:var(--teal)}
.links .site{color:var(--navy)}
</style>
</head>
<body>
<div class="alert-bar"><span>Coronavirus Disease 2019 (COVID-19) Total COVID-19 Tests Performed - 654,249</span><span class="read">Read More</span></div>
<div class="alert-close">X</div>

<header class="site-header">
  <div class="brand"><span class="dot"></span>Harbor Ridge Laboratories</div>
  <div class="contact" style="left:332px"><svg viewBox="0 0 24 24"><path d="M6 3l4 4-2 3a12 12 0 006 6l3-2 4 4-3 3C9 21 3 15 3 6z" fill="#999"/></svg><div><b>Telephone</b><span>800-555-0142 (800-555-0142)</span></div></div>
  <div class="contact" style="left:490px"><svg viewBox="0 0 24 24"><rect x="2" y="5" width="20" height="14" fill="none" stroke="#999" stroke-width="2"/><path d="M2 5l10 8 10-8" fill="none" stroke="#999" stroke-width="2"/></svg><div><b>Email Address</b><span>info@harborridgelabs.example</span></div></div>
  <div class="contact" style="left:636px"><svg viewBox="0 0 24 24"><path d="M12 2a7 7 0 017 7c0 5-7 13-7 13S5 14 5 9a7 7 0 017-7z" fill="#999"/><circle cx="12" cy="9" r="2.5" fill="#fff"/></svg><div><b>Corporate Headquarters</b><span>410 Harbor Ave Brooklyn NY 11200</span></div></div>
</header>

<nav class="main-nav">
  <span class="item" style="left:11px;top:20px">About Us</span>
  <span class="item" style="left:69px;top:20px">Patient Services ▾</span>
  <span class="item" style="left:11px;top:55px">COVID-19</span>
  <div class="book">Book Appointment<br>Online</div>
</nav>

<section class="hero" role="img" aria-label="Laboratory scientist working at a bench">
  <h1>The World of<br>Diagnostics</h1>
  <p>Interested in signing up?</p>
  <div class="cta" style="left:16px;width:124px">PORTAL<br>Access</div>
  <div class="cta" style="left:190px;width:104px"></div>
  <div class="cta" style="left:345px;width:104px"></div>
</section>

<section class="intro">
  <h2>Tests designed for <em>Your Convenience.</em></h2>
  <hr>
  <p>Harbor Ridge Laboratories is pleased to offer its services to you and your patients. You can use our webpage to learn about the services we provide from the comfort of your own home. Harbor Ridge Laboratories provides numerous patient services with convenient hours. Our secure electronic health records guarantee confidential information for you and your patients by increasing lab productivity and providing you with the support and information that you need.</p>
</section>

<article class="card" style="left:72px">
  <div class="photo" role="img" aria-label="Lab technician at a microscope" style="background:linear-gradient(135deg,#dfe6ea,#aab8c2)"></div>
  <h3>Integrated Genetic<strong>Solutions</strong></h3>
  <p>IGS provides a comprehensive and fully customized solution to help you reach your ideal mental and physical potential.</p>
</article>
<article class="card" style="left:419px">
  <div class="photo" role="img" aria-label="Gloved hands handling lab equipment" style="background:linear-gradient(135deg,#8a8e90,#e6e8e6)"></div>
  <h3>Always Available<strong>For You</strong></h3>
  <p>We're there for you 24/7. Click here to ask anything about our methods and equipment.</p>
</article>

<footer class="site-footer">
  <div class="brand"><span class="dot"></span>Harbor Ridge Laboratories</div>
  <p class="about">Harbor Ridge Laboratories is dedicated to providing superior service to your medical practice.</p>
  <div class="newsletter">
    <h4>Subscribe to our Newsletter</h4>
    <div class="field" style="left:420px">Your Name</div>
    <div class="field" style="left:546px">Your Email</div>
    <div class="sub">SUBSCRIBE</div>
  </div>
</footer>
<div class="legal">© 2008-2020 Harbor Ridge Laboratories, Inc. All Rights Reserved. HRL and Harbor Ridge Laboratories are registered trademarks of Harbor Ridge Laboratories®, Inc.</div>

<div class="shade"></div>

<div class="modal">
  <div class="photo" role="img" aria-label="Two scientists examining a flask in a laboratory"></div>
  <div class="body">
    <div class="brand"><span class="dot"></span>Harbor Ridge Laboratories</div>
    <p>we are&nbsp; partnership with VELARA, a large Dominican community healthcare service in the greater NYC area.</p>
    <div class="signup"><span>Enter Email Address</span><div class="send"><svg width="15" height="15" viewBox="0 0 24 24"><path d="M22 2L2 11l7 3 2 7 3-5 5 3z" fill="#fff"/></svg></div></div>
    <div class="links"><a class="learn" href="#">LEARN MORE ➔</a><a class="site" href="#">GO TO WEBSITE ●</a></div>
  </div>
</div>
</body>
</html>
```